Paper Tides - post rock band album cover design

We are Paper Tides, a post-rock band based on San Jose, CA, USA. We will release a new album “Where the rivers fold" and need a album cover.

The new album is full of emotion and energy. song list:
1. Forward
2. Search (in uploaded files)
3. Before
4. Memory
5. Dream
6. Spring
7. Om Namah Shivaya

Please hear our previous music here
https://paper-tides.soundvault-example.com/album/paper-tides

Target Market(s)

music lovers

Industry/Entity Type

Music Download

Colors

Designer to choose colors to be used in the design.

Requirements
Must have
• album cover + back
• For cover we only need band name (do not need album name), want to use some streamline font for the band name "Paper Tides"
• I attached an example from another band
Nice to have
• I don't want to limit the designers, so please listen to the music and design what you feel the best:)

```html
<!DOCTYPE html>
<html lang="en">
<head>
<meta charset="utf-8">
<title>Paper Tides – Album Cover and Back</title>
<link rel="stylesheet" href="https://fonts.googleapis.com/css2?family=Pinyon+Script&display=swap">
<style>
  :root {
    --page-bg: #ededed;
    --gold-light: #fff36a;
    --gold: #f2d600;
    --amber: #e8a21a;
    --ember: #b55a12;
    --maroon-light: #7a1c0e;
    --maroon: #4a0c06;
    --night: #170302;
    --ink-brown: #5a1a08;
    --white: #ffffff;
    --disc-rim: #3a1a08;
  }
  * { box-sizing: border-box; margin: 0; padding: 0; }
  html, body { width: 1200px; height: 1200px; overflow: hidden; }
  body {
    background: var(--page-bg);
    font-family: "Pinyon Script", cursive;
    position: relative;
  }

  /* Sleeve spread: back, spine, front */
  .sleeve {
    position: absolute;
    left: 164px;
    top: 90px;
    display: flex;
    height: 420px;
  }
  .back-cover {
    position: relative;
    width: 420px;
    height: 420px;
    background:
      linear-gradient(160deg, var(--night) 0%, var(--maroon) 35%, var(--maroon-light) 65%, var(--maroon) 100%);
    overflow: hidden;
  }
  .back-art {
    position: absolute;
    inset: 0;
    background:
      linear-gradient(200deg, rgba(180,60,30,0) 40%, rgba(190,70,35,.45) 55%, rgba(180,60,30,0) 70%),
      linear-gradient(165deg, rgba(150,40,20,0) 60%, rgba(160,50,25,.4) 75%, rgba(150,40,20,0) 90%);
  }
  .track-list {
    position: absolute;
    left: 46px;
    bottom: 40px;
    list-style: none;
    color: var(--white);
    font-size: 17px;
    line-height: 18px;
  }
  .back-marks {
    position: absolute;
    right: 30px;
    bottom: 42px;
    display: flex;
    gap: 22px;
    align-items: center;
    color: var(--white);
    font-size: 18px;
  }

  .spine {
    position: relative;
    width: 32px;
    height: 420px;
    background: linear-gradient(180deg, var(--amber) 0%, var(--gold) 30%, var(--amber) 70%, var(--ember) 100%);
  }
  .spine-title {
    position: absolute;
    left: 50%;
    top: 150px;
    transform: translateX(-50%) rotate(-90deg);
    transform-origin: center;
    white-space: nowrap;
    color: var(--ink-brown);
    font-size: 18px;
  }

  .front-cover {
    position: relative;
    width: 420px;
    height: 420px;
    overflow: hidden;
  }
  .front-art {
    position: absolute;
    inset: 0;
    background:
      radial-gradient(circle at 52% 78%, rgba(255,255,230,.95) 0%, rgba(255,240,140,.6) 8%, rgba(255,240,140,0) 22%),
      radial-gradient(circle at 60% 40%, var(--gold-light) 0%, var(--gold) 40%, var(--amber) 75%, var(--ember) 100%);
  }
  .front-title {
    position: absolute;
    left: 175px;
    top: 255px;
    color: var(--ink-brown);
    font-size: 60px;
    line-height: 40px;
  }
  .front-title span { display: block; }
  .front-title .line-one { padding-left: 70px; }

  /* Disc label */
  .disc {
    position: absolute;
    left: 380px;
    top: 630px;
    width: 440px;
    height: 440px;
    border-radius: 50%;
    border: 2px solid var(--disc-rim);
    background:
      radial-gradient(circle at 55% 85%, rgba(255,255,230,.9) 0%, rgba(255,240,140,0) 20%),
      radial-gradient(circle at 60% 35%, var(--gold-light) 0%, var(--gold) 40%, var(--amber) 75%, var(--ember) 100%);
    overflow: hidden;
  }
  .disc-art { position: absolute; inset: 0; }
  .disc-hole {
    position: absolute;
    left: 50%;
    top: 50%;
    width: 186px;
    height: 186px;
    margin: -93px 0 0 -93px;
    border-radius: 50%;
    background: var(--page-bg);
    border: 1px solid var(--disc-rim);
  }
  .disc-title {
    position: absolute;
    left: 0;
    right: 0;
    top: 50px;
    text-align: center;
    color: var(--ink-brown);
    font-size: 40px;
  }
  .disc-title-faint {
    position: absolute;
    left: 0;
    right: 0;
    bottom: 50px;
    text-align: center;
    color: var(--ink-brown);
    opacity: .35;
    font-size: 30px;
  }
  .disc-mark {
    position: absolute;
    top: 205px;
    color: var(--ink-brown);
    font-size: 22px;
  }
  .disc-mark.left { left: 30px; }
  .disc-mark.right { right: 34px; }
</style>
</head>
<body>

<section class="sleeve" aria-label="Album sleeve, back, spine and front">
  <div class="back-cover">
    <div class="back-art" role="img" aria-label="Dark red abstract light streaks flowing diagonally"></div>
    <ol class="track-list">
      <li>1. Forward</li>
      <li>2. Search (in uploaded files)</li>
      <li>3. Before</li>
      <li>4. Memory</li>
      <li>5. Dream</li>
      <li>6. Spring</li>
      <li>7. Om Namah Shivaya</li>
    </ol>
    <div class="back-marks">
      <span class="mark">Audio Disc</span>
      <span class="mark">OptiDisc</span>
    </div>
  </div>

  <div class="spine">
    <span class="spine-title">Paper Tides</span>
  </div>

  <div class="front-cover">
    <div class="front-art" role="img" aria-label="Golden yellow burst of light rays with soft bokeh sparkles"></div>
    <h1 class="front-title"><span class="line-one">Paper</span><span>Tides</span></h1>
  </div>
</section>

<section class="disc" aria-label="Disc label">
  <div class="disc-art" role="img" aria-label="Golden light rays and glowing flare"></div>
  <div class="disc-title">Paper Tides</div>
  <div class="disc-mark left">Audio Disc</div>
  <div class="disc-mark right">OptiDisc</div>
  <div class="disc-title-faint">Paper Tides</div>
  <div class="disc-hole"></div>
</section>

</body>
</html>
```